依頼詳細
弊社オリジナルのコンセプト企画住宅をプロデュースするにあたり
お客様にお渡しする資料として使用するリーフレットの制作をお願いします。
「樹影」にはまだカタログやパンフレットが無いので、このリーフレットがお客様への最初のご案内・ご紹介になります。
記載項目
松葉建築株式会社 代表取締役 堀内宗一 お問合せ 0297-61-3027 sora@matsuba-kenchiku.jp
サイズ
A3
ページ数
両面
希望イメージ
シンプル 複雑
単色 カラフル
暗い 明るい
日常 高級
遊び心 厳粛
未来的 伝統的
女性的 男性的
希望する色
納品ファイル
• イラストレーター形式 (.ai)
補足説明
下記のフォルダに、必要なファイルを入れました。
https://files.hokuyo-share.net/f/7Qp2XkLm9RtVw4Zc8Nd3sJb6Hy1Ga5Ue?mode=view
■ 選んだ理由

ご提案いただいた中には、メッセージで協調してくれたいいご提案もあったのですが、内容ボリュームが薄い中で、内容に充実感が感じられたり、その内容とページに集中できる設計になっていたので、読んでいただけるのかなと思いまして選びました

インパクトがあったので決めました。

■ 提案者全員のお礼・コメント

皆さま、ご提案ありがとうございました。 今後もあらたなコンセプトで様々な広告をお願いしようと思っておりますので、どうぞよろしくお願いします!

```html
<!DOCTYPE html>
<html lang="ja">
<head>
<meta charset="utf-8">
<title>樹影 コンセプトブック</title>
<link href="https://fonts.googleapis.com/css2?family=Noto+Sans+JP:wght@400;500;700;900&family=Noto+Serif+JP:wght@500;700;900&display=swap" rel="stylesheet">
<style>
  :root {
    --paper: #ffffff;
    --ink: #2b2b2b;
    --leaf: #93b46a;
    --leaf-deep: #3a4529;
    --band: #3d4a2f;
    --white: #ffffff;
  }
  html, body { margin: 0; padding: 0; overflow: hidden; background: var(--paper); }
  .sheet {
    position: relative;
    width: 853px; height: 1200px;
    background: var(--paper);
    overflow: hidden;
    font-family: "Noto Sans JP", sans-serif;
    color: var(--ink);
  }
  .lead {
    position: absolute; left: 0; right: 0; top: 42px;
    text-align: center; margin: 0;
    font-size: 20px; font-weight: 700; letter-spacing: 0.08em;
  }
  .tagline {
    position: absolute; left: 0; right: 0; top: 112px;
    text-align: center; margin: 0;
    font-size: 27px; font-weight: 700; letter-spacing: 0.06em;
  }
  .concept-label {
    position: absolute; left: 84px; top: 178px;
    width: 196px; height: 42px; box-sizing: border-box;
    border: 1.5px solid var(--ink);
    display: flex; align-items: center; justify-content: center;
    font-size: 19px; font-weight: 700; letter-spacing: 0.04em;
  }
  .product-name {
    position: absolute; left: 84px; top: 240px; width: 196px;
    margin: 0; text-align: center;
    font-family: "Noto Serif JP", serif; font-weight: 700;
  }
  .product-char { display: block; font-size: 86px; line-height: 1; }
  .product-reading {
    display: block; margin: 26px 0 60px;
    font-family: "Noto Sans JP", sans-serif; font-weight: 400;
    font-size: 13px; letter-spacing: 0.6em;
  }
  .panel {
    position: absolute; left: 326px; top: 236px;
    width: 386px; height: 560px;
    background: var(--leaf);
  }
  .panel-kicker {
    position: absolute; left: 0; right: 0; top: 40px;
    text-align: center; margin: 0;
    color: var(--white); font-size: 17px; font-weight: 700; letter-spacing: 0.08em;
  }
  .panel-title {
    position: absolute; left: 0; right: 0; top: 76px;
    text-align: center; margin: 0;
    color: var(--white);
    font-family: "Noto Serif JP", serif; font-weight: 700;
    font-size: 84px; line-height: 1.05; letter-spacing: 0.02em;
  }
  .panel-phrase {
    position: absolute; right: 40px; top: 270px;
    margin: 0;
    writing-mode: vertical-rl;
    color: var(--leaf-deep); font-size: 21px; font-weight: 700;
    letter-spacing: 0.4em; line-height: 1.9;
  }
  .house-view {
    position: absolute; left: 0; top: 700px;
    width: 853px; height: 350px;
    background: linear-gradient(180deg, rgba(255,255,255,0) 0%, rgba(201,214,178,0.6) 18%, #7f8c6a 45%, #4a4a46 62%, #d9d9d4 85%, #ffffff 100%);
  }
  .booklet-band {
    position: absolute; left: 226px; top: 1048px;
    width: 402px; height: 34px;
    background: var(--band);
    color: var(--white);
    display: flex; align-items: center; justify-content: center;
    font-size: 16px; font-weight: 700; letter-spacing: 0.06em;
  }
  .brand {
    position: absolute; left: 0; right: 0; top: 1100px;
    display: flex; align-items: center; justify-content: center; gap: 10px;
    font-size: 22px; font-weight: 900; letter-spacing: 0.12em; color: var(--ink);
  }
  .brand-dot { width: 18px; height: 18px; border-radius: 50%; background: var(--ink); }
</style>
</head>
<body>
<div class="sheet">
  <p class="lead">設計士が２度目に建てたい家</p>
  <p class="tagline">樹影のなかで変化を楽しみながら生きる家</p>

  <div class="concept-label">コンセプト企画住宅</div>
  <h1 class="product-name">
    <span class="product-char">樹</span>
    <span class="product-reading">じゅえい</span>
    <span class="product-char">影</span>
  </h1>

  <section class="panel">
    <p class="panel-kicker">私の家はアートギャラリー</p>
    <h2 class="panel-title">森光自然<br>調和住宅</h2>
    <p class="panel-phrase">自然に逆らわずに<br>生きる家</p>
  </section>

  <div class="house-view" role="img" aria-label="平屋の住宅外観パース、植栽と駐車場の車、人物のいる前庭"></div>

  <div class="booklet-band">建築パース・コンセプトブック</div>

  <div class="brand"><span class="brand-dot"></span><span>MATSUBA</span></div>
</div>
</body>
</html>
```